New Business Card Design Project

We would like a business card that represents the sale of boat, home, auto, and life insurance.

The logo can change colors to meet the look of the design if needed.

Industry/Entity Type

Business

```html
<!DOCTYPE html>
<html lang="en">
<head>
<meta charset="utf-8">
<title>Meridian Financial – Business Card</title>
<link href="https://fonts.googleapis.com/css2?family=Questrial&display=swap" rel="stylesheet">
<style>
  :root {
    --backdrop: #e9ebec;
    --teal: #3f7689;
    --paper: #ffffff;
    --ink: #2b2b2b;
    --strip: #3b3b3b;
    --on-teal: #ffffff;
    --on-teal-soft: #d8e6eb;
  }
  * { box-sizing: border-box; margin: 0; padding: 0; }
  html, body {
    width: 1200px; height: 676px; overflow: hidden;
    background: var(--backdrop);
    font-family: "Questrial", "Century Gothic", sans-serif;
  }
  .sheet {
    position: relative; width: 1200px; height: 676px;
    display: flex; align-items: center; justify-content: center; gap: 40px;
  }
  .card {
    position: relative; width: 540px; height: 309px; overflow: hidden;
    box-shadow: 0 6px 18px rgba(0,0,0,.18);
  }

  /* Brand name: one colour, one weight, one line */
  .brand {
    display: flex; align-items: center; gap: 10px; white-space: nowrap;
  }
  .brand-dot { flex: none; border-radius: 50%; background: currentColor; }
  .brand-name { font-size: inherit; letter-spacing: 0; line-height: 1; }

  /* Front */
  .card-front { background: var(--teal); }
  .front-brand {
    position: absolute; left: 230px; top: 130px;
    color: var(--on-teal); font-size: 30px;
  }
  .front-brand .brand-dot { width: 22px; height: 22px; }

  /* Back */
  .card-back { background: var(--teal); }
  .back-brand-panel {
    position: absolute; left: 0; top: 0; width: 240px; height: 100%;
    background: var(--paper);
    display: flex; align-items: center; justify-content: center;
  }
  .back-brand { color: var(--ink); font-size: 19px; gap: 8px; }
  .back-brand .brand-dot { width: 14px; height: 14px; }

  .icon-strip {
    position: absolute; left: 240px; top: 150px; width: 26px; height: 159px;
    background: var(--strip);
    display: flex; flex-direction: column; align-items: center; padding-top: 8px; gap: 12px;
  }
  .icon-strip svg { width: 12px; height: 12px; display: block; }

  .contact-panel {
    position: absolute; left: 282px; top: 92px; right: 20px; color: var(--on-teal);
  }
  .person-name { font-size: 22px; line-height: 1.1; }
  .person-role { font-size: 12px; color: var(--on-teal-soft); }
  .contact-list { list-style: none; margin-top: 38px; font-size: 13.5px; line-height: 1.28; }
</style>
</head>
<body>
<main class="sheet">

  <section class="card card-front" aria-label="Card front">
    <div class="brand front-brand">
      <span class="brand-dot"></span>
      <span class="brand-name">Meridian Financial</span>
    </div>
  </section>

  <section class="card card-back" aria-label="Card back">
    <div class="back-brand-panel">
      <div class="brand back-brand">
        <span class="brand-dot"></span>
        <span class="brand-name">Meridian Financial</span>
      </div>
    </div>

    <div class="icon-strip" aria-hidden="true">
      <svg viewBox="0 0 12 12"><path d="M6 1a3.5 3.5 0 0 0-3.5 3.5C2.5 7.5 6 11 6 11s3.5-3.5 3.5-6.5A3.5 3.5 0 0 0 6 1z" fill="#fff"/><circle cx="6" cy="4.5" r="1.2" fill="#3b3b3b"/></svg>
      <svg viewBox="0 0 12 12"><rect x="3" y="1" width="6" height="10" rx="1" fill="#fff"/><rect x="4" y="2.5" width="4" height="5.5" fill="#3b3b3b"/></svg>
      <svg viewBox="0 0 12 12"><rect x="1.5" y="1.5" width="9" height="9" fill="none" stroke="#fff" stroke-width="1.2"/></svg>
      <svg viewBox="0 0 12 12"><rect x="1" y="2.5" width="10" height="7" fill="#fff"/><path d="M1 2.5l5 4 5-4" fill="none" stroke="#3b3b3b" stroke-width="1"/></svg>
      <svg viewBox="0 0 12 12"><circle cx="6" cy="6" r="4.5" fill="none" stroke="#fff" stroke-width="1"/><ellipse cx="6" cy="6" rx="2" ry="4.5" fill="none" stroke="#fff" stroke-width="1"/><path d="M1.5 6h9" stroke="#fff" stroke-width="1"/></svg>
    </div>

    <div class="contact-panel">
      <p class="person-name">your name</p>
      <p class="person-role">designation</p>
      <ul class="contact-list">
        <li>address (street address</li>
        <li>suite number, city, state, zip</li>
        <li>0123 456 789</li>
        <li>0123 456 789</li>
        <li>youremail@example.com</li>
        <li>www.yourwebsite.com</li>
      </ul>
    </div>
  </section>

</main>
</body>
</html>
```